new website for ISP and tech consultant

Our company is a wireless Internet Service Provider as well as a technology consultant. We need a new website that is modern looking and something that I can make responsive and mobile friendly. All the pages that are at on our current website (kadimo.com) must also exist on the new site so please allow space for navigation for them in the design.

It's OK to change logo color

Target Market(s)

Rural internet customers

Industry/Entity Type

Internet Service Provider

Number of Pages Required

1 page

Font styles to use
Sans Serif

Requirements
Must have
• Please keep in mind with the design will need to be able to be made mobile friendly and responsive.
• I'd like an "edge to edge" look in the browser.
• Integrate our logo and the "field" picture (attached)
Should not have
• stock photos (as little as possible)

```html
<!DOCTYPE html>
<html lang="en">
<head>
<meta charset="utf-8">
<title>Kadimo High-Speed Internet</title>
<link href="https://fonts.googleapis.com/css2?family=Lato:wght@300;400;700;900&display=swap" rel="stylesheet">
<style>
:root{
  --blue:#2f5fb7;
  --blue-dark:#244c9a;
  --ink:#2b2b2b;
  --card-top:#2b2b2b;
  --card-mid:#1c1c1c;
  --footer:#202020;
  --line:#e2e2e2;
}
*{margin:0;padding:0;box-sizing:border-box}
html,body{width:890px;height:1200px;overflow:hidden;background:#fff}
body{font-family:'Lato',sans-serif;color:var(--ink);position:relative}
.abs{position:absolute}
.topbar{left:0;top:0;width:890px;height:28px;background:var(--blue);color:#fff}
.topbar .tag{left:136px;top:9px;font-size:9px}
.topbar .mail{left:589px;top:8px;font-size:10px}
.topbar .phone{left:669px;top:8px;font-size:10.5px;display:flex;gap:4px;align-items:center}
.header{left:0;top:28px;width:890px;height:67px;background:linear-gradient(#fff,#f1f1f1);border-bottom:2px solid #3a3a3a}
.brand{display:flex;align-items:center;gap:6px;font-weight:700;font-size:15px;color:var(--blue)}
.brand .dot{width:14px;height:14px;border-radius:50%;background:var(--blue)}
.header .brand{left:136px;top:24px}
.nav{display:flex;gap:12px;font-size:9.5px;color:#444}
.header .nav{left:383px;top:27px}
.hero{left:0;top:95px;width:890px;height:313px;background:linear-gradient(180deg,#8fb6de 0%,#c9dcef 38%,#6d9440 52%,#4f7a2c 75%,#6b4a2e 100%)}
.person{left:470px;top:128px;width:300px;height:250px;background:linear-gradient(135deg,#e3dccd,#7f9cc8);opacity:.55}
.hero-title{left:136px;top:145px;color:#fff;font-size:30px;line-height:39px;font-weight:700;text-shadow:0 1px 3px rgba(0,0,0,.4)}
.hero-sub{left:137px;top:266px;color:#fff;font-size:12.5px;font-weight:700;text-shadow:0 1px 3px rgba(0,0,0,.5)}
.join{left:137px;top:296px;width:84px;height:30px;background:#fff;border-radius:2px;color:var(--blue-dark);font-size:10.5px;font-weight:700;display:flex;align-items:center;justify-content:center}
.intro{left:136px;top:444px;width:142px}
.intro h2{font-weight:300;font-size:16.5px;line-height:22.5px;color:#333}
.intro p{font-size:7.5px;line-height:12.8px;color:#555;margin-top:6px}
.vsep{width:1px;background:var(--line)}
.feature{width:150px;text-align:center;font-size:11px;font-weight:700;line-height:15.5px;color:#333}
.feature svg{display:block;margin:0 auto 8px}
.deals{left:133px;top:598px}
.deals h2{font-size:25px;font-weight:700;color:#333;letter-spacing:-.3px}
.deals h3{font-size:12px;font-weight:700;color:#333;margin-top:4px}
.search{left:612px;top:603px;width:141px;height:42px;display:flex}
.search .field{flex:1;background:#ececec;color:#999;font-size:10px;padding:15px 10px}
.search .go{width:41px;background:var(--blue);display:flex;align-items:center;justify-content:center}
.plan{width:195px;top:684px;height:135px}
.plan .speed{height:42px;background:var(--card-top);color:#fff;font-size:20px;font-weight:700;padding:11px 17px}
.plan .desc{height:48px;background:var(--card-mid);color:#fff;font-size:9.5px;line-height:16.5px;padding:7px 17px}
.plan .price{height:45px;background:var(--blue);color:#fff;font-size:26px;font-weight:700;padding:6px 16px}
.plan .price small{font-size:16px;font-weight:400;font-style:italic}
.hline{left:136px;top:838px;width:618px;height:1px;background:var(--line)}
.col h4{font-size:13px;font-weight:700;color:#222}
.it h4{font-size:18px;font-weight:900}
.col p{font-size:7.5px;line-height:12.8px;color:#444}
.news .date{font-size:12px;font-weight:700;margin-bottom:2px}
.links{list-style:none;font-size:8px;color:var(--blue)}
.links li{height:22.2px}
.links li::before{content:"» "}
.thumb{left:134px;top:965px;width:92px;height:64px;background:#ececec}
.quote{left:233px;top:965px;width:88px;font-size:7.5px;line-height:9.6px;color:#444}
.quote b{display:block;font-weight:700;color:#222;margin-top:5px}
.footer{left:0;top:1054px;width:890px;height:146px;background:var(--footer)}
.foot-brand{left:160px;top:1113px;color:#fff;font-size:17px}
.foot-brand .dot{background:#fff}
.foot-nav{left:265px;top:1089px;color:#ddd;font-size:9.5px;gap:9px}
.foot-rule{left:265px;top:1112px;width:476px;height:1px;background:#555}
.foot-sign{left:264px;top:1132px;color:#fff;font-size:11.5px}
.input{top:1128px;width:123px;height:23px;background:#f1f1f1;font-size:7.5px;color:#888;padding:7px 8px}
.submit{left:642px;top:1128px;width:97px;height:23px;background:var(--blue);color:#fff;font-size:8px;font-weight:700;display:flex;align-items:center;justify-content:center}
</style>
</head>
<body>
<div class="abs topbar">
  <span class="abs tag">KADIMO HIGH-SPEED INTERNET</span>
  <span class="abs mail">info@kadimo.com</span>
  <span class="abs phone"><svg width="8" height="8" viewBox="0 0 10 10"><path d="M2 0l2 2.5-1.2 1.2a6 6 0 003.5 3.5L7.5 6 10 8l-1.5 2C4 10 0 6 0 1.5z" fill="#fff"/></svg>555-014-2290</span>
</div>
<div class="abs header">
  <div class="abs brand"><span class="dot"></span>Kadimo</div>
  <nav class="abs nav"><span>Home</span><span>Internet</span><span>Services</span><span>Products</span><span>Pay your bill</span><span>Email</span><span>Support</span><span>Contact</span><span>News</span></nav>
</div>
<div class="abs hero" role="img" aria-label="Photo of a green rural field under a blue sky"></div>
<div class="abs person" role="img" aria-label="Photo of a young man kneeling on a dirt path working on a laptop"></div>
<h1 class="abs hero-title">High-Speed wireless<br>Internet starting at<br>$49.95/month</h1>
<div class="abs hero-sub">NO arbitrary data cap! * No hidden fees!</div>
<div class="abs join">Join Now</div>

<div class="abs intro">
  <h2>Fast download &amp; upload speeds at an affordable price</h2>
  <p>Praesent vestibulum aenean nonummy hendrerit mauris. Cum sociis natoque penatibus et magnis dis parturient montes ascetur ridiculus mus. Nulla dui.</p>
</div>
<div class="abs vsep" style="left:286px;top:445px;height:118px"></div>
<div class="abs vsep" style="left:442px;top:462px;height:76px"></div>
<div class="abs vsep" style="left:603px;top:462px;height:76px"></div>

<div class="abs feature" style="left:292px;top:458px">
  <svg width="50" height="46" viewBox="0 0 50 46" fill="var(--blue)"><g stroke="var(--blue)" stroke-width="4"><path d="M16 9v26M3 22h26M7 13l18 18M25 13L7 31"/></g><circle cx="16" cy="22" r="10"/><circle cx="16" cy="22" r="4" fill="#fff"/><circle cx="36" cy="10" r="7"/><circle cx="36" cy="10" r="2.5" fill="#fff"/><circle cx="37" cy="35" r="7"/><circle cx="37" cy="35" r="2.5" fill="#fff"/></svg>
  Equipment Installation<br>and Setup
</div>
<div class="abs feature" style="left:448px;top:447px">
  <svg width="54" height="56" viewBox="0 0 54 56"><path d="M8 30a19 19 0 0138 0" fill="none" stroke="var(--blue)" stroke-width="5"/><rect x="4" y="27" width="9" height="16" rx="3" fill="var(--blue)"/><rect x="41" y="27" width="9" height="16" rx="3" fill="var(--blue)"/><path d="M45 43q0 8-12 9" fill="none" stroke="var(--blue)" stroke-width="2.5"/><circle cx="31" cy="52" r="3" fill="var(--blue)"/></svg>
  Castomer Support<br>Center
</div>
<div class="abs feature" style="left:608px;top:460px">
  <svg width="44" height="42" viewBox="0 0 44 42" fill="var(--blue)"><rect x="4" y="20" width="8" height="18"/><path d="M14 20l8-12c2-4 6-4 6 0l-1 8h10c3 0 4 3 3 5l-3 14c-1 3-3 3-5 3H14z"/></svg>
  Customer<br>Guarantee
</div>

<div class="abs deals">
  <h2>FIND THE BEST DEALS IN YOUR AREA</h2>
  <h3>ENTER YOUR PLANS AND GET PRICE DETAILES</h3>
</div>
<div class="abs search"><div class="field">Enter Here</div><div class="go"><svg width="8" height="12" viewBox="0 0 8 12"><path d="M0 0l8 6-8 6z" fill="#fff"/></svg></div></div>

<div class="abs plan" style="left:136px"><div class="speed">2 Mbps</div><div class="desc">ACCESS TO 100,000 WIFI<br>HOTSPOTS AT NO EXTRA COST</div><div class="price">$25.99/<small>Month</small></div></div>
<div class="abs plan" style="left:347px"><div class="speed">5 Mbps</div><div class="desc">ACCESS TO 100,000 WIFI<br>HOTSPOTS AT NO EXTRA COST</div><div class="price">$45.99/<small>Month</small></div></div>
<div class="abs plan" style="left:559px"><div class="speed">10 Mbps</div><div class="desc">ACCESS TO 100,000 WIFI<br>HOTSPOTS AT NO EXTRA COST</div><div class="price">$65.99/<small>Month</small></div></div>
<div class="abs hline"></div>

<div class="abs col it" style="left:136px;top:855px;width:196px">
  <h4>NEED IT SOLUTIONS?</h4>
  <p style="margin-top:6px">Lorem ipsum dolor sit amet, consectetur adipisicing elit, sed do eiusmod tempor incididunt ut labore et dolore magna aliqua. Ut enim ad minim veniam, quis nostrud exercitation ullamco laboris nisi ut aliquip commodo consequat. Duis aute irure dolor in reprehenderit in voluptate velit esse.</p>
</div>
<div class="abs thumb" role="img" aria-label="Portrait photo of the quoted director"></div>
<div class="abs quote">“ Aenean nonummy hendrerit mau phasellu porta. Fusce Aenean nonummy hendrerit mau phasellu porta. ”<b>Dana Whitfield, Director</b></div>

<div class="abs col news" style="left:347px;top:857px;width:190px">
  <h4>NEWS &amp; EVENTS:</h4>
  <div class="date" style="margin-top:9px">03/14</div>
  <p>laboris nisi ut aliquip commodo consequat. Duis aute irure dolor in reprehenderit in voluptate velit esse. laboris nisi ut aliquip commodo consequat. Duis aute irure dolor in reprehenderit in voluptate velit esse.</p>
  <div class="date" style="margin-top:12px">03/14</div>
  <p>laboris nisi ut aliquip commodo consequat. Duis aute irure dolor in reprehenderit in voluptate velit esse. laboris nisi ut aliquip commodo consequat. Duis aute irure dolor in reprehenderit in voluptate velit esse.</p>
</div>
<div class="abs col" style="left:558px;top:856px">
  <h4 style="font-size:11.5px">FEATURED:</h4>
  <ul class="links" style="margin-top:10px"><li>Managed Services</li><li>Virtual Office</li><li>Strategic Planning</li><li>Installation</li><li>Mobile IT</li><li>Network Security</li></ul>
</div>
<div class="abs col" style="left:665px;top:856px">
  <h4 style="font-size:11.5px">POPULAR:</h4>
  <ul class="links" style="margin-top:10px"><li>Managed Services</li><li>Virtual Office</li><li>Strategic Planning</li><li>Installation</li><li>Mobile IT</li><li>Network Security</li></ul>
</div>

<footer class="abs footer"></footer>
<div class="abs brand foot-brand"><span class="dot"></span>Kadimo</div>
<nav class="abs nav foot-nav"><span>Home</span><span>Internet</span><span>Services</span><span>Products</span><span>Pay your bill</span><span>Email</span><span>Support</span><span>Contact</span><span>News</span></nav>
<div class="abs foot-rule"></div>
<div class="abs foot-sign">Signup Newslatter</div>
<div class="abs input" style="left:373px">Enter Name</div>
<div class="abs input" style="left:507px">Enter Email</div>
<div class="abs submit">SUBMIT</div>
</body>
</html>
```